Business card for a new cabinet shop company named Marlowe Cabinets for high end cabinets

Design a business card, thinking dark rich green with colours to speak of high end luxury ie; cream, gold, black possibly

Peter Lindqvar
Director Craftsman
Email: info@marlowecabinets.com.au
Instagram : @marlowe.cabinets

```html
<!DOCTYPE html>
<html lang="en">
<head>
<meta charset="utf-8">
<title>Marlowe Cabinets – Business Card</title>
<link rel="stylesheet" href="https://fonts.googleapis.com/css2?family=Poppins:wght@300;400&family=Russo+One&display=swap">
<style>
  :root {
    --page: #fefefe;
    --gold: #c9ab66;
    --black: #050505;
    --white: #ffffff;
  }
  * { box-sizing: border-box; margin: 0; padding: 0; }
  html, body {
    width: 1200px;
    height: 1200px;
    overflow: hidden;
    background: var(--page);
  }
  .sheet {
    position: relative;
    width: 1200px;
    height: 1200px;
  }
  .card {
    position: absolute;
    top: 486px;
    width: 410px;
    height: 235px;
    background: var(--gold);
    border-radius: 9px;
    overflow: hidden;
    font-family: "Poppins", sans-serif;
  }
  .card--front { left: 177px; }
  .card--back  { left: 620px; }

  .card__body {
    position: absolute;
    left: 0;
    right: 0;
    top: 5px;
    bottom: 5px;
    background: var(--black);
    border-radius: 4px;
  }

  /* Front */
  .brand {
    position: absolute;
    left: 0;
    right: 0;
    top: 50%;
    transform: translateY(-50%);
    display: flex;
    align-items: center;
    justify-content: center;
    gap: 12px;
  }
  .brand__mark {
    width: 18px;
    height: 18px;
    background: var(--gold);
  }
  .brand__name {
    color: var(--gold);
    font-weight: 400;
    font-size: 30px;
    letter-spacing: 0.5px;
  }

  /* Back */
  .name-panel {
    position: absolute;
    left: 76px;
    width: 258px;
    top: 0;
    height: 141px;
    background: var(--gold);
    text-align: center;
  }
  .name-panel__name {
    position: absolute;
    left: 0;
    right: 0;
    top: 89px;
    color: var(--white);
    font-family: "Russo One", sans-serif;
    font-size: 21px;
    line-height: 1;
    letter-spacing: 0.5px;
  }
  .name-panel__title {
    position: absolute;
    left: 0;
    right: 0;
    top: 112px;
    color: var(--white);
    font-weight: 300;
    font-size: 11px;
    line-height: 1;
    letter-spacing: 0.2px;
  }
  .contact {
    position: absolute;
    left: 0;
    right: 0;
    top: 158px;
    text-align: center;
    font-size: 10.5px;
    font-weight: 300;
    line-height: 17px;
    color: var(--white);
  }
  .contact__label { color: var(--gold); }
  .foot-band {
    position: absolute;
    left: 76px;
    width: 258px;
    bottom: 0;
    height: 24px;
    background: var(--gold);
  }
</style>
</head>
<body>
<main class="sheet">
  <section class="card card--front" aria-label="Business card front">
    <div class="card__body">
      <div class="brand">
        <span class="brand__mark" aria-hidden="true"></span>
        <span class="brand__name">Marlowe Cabinets</span>
      </div>
    </div>
  </section>

  <section class="card card--back" aria-label="Business card back">
    <div class="card__body"></div>
    <div class="name-panel">
      <h1 class="name-panel__name">PETER LINDQVAR</h1>
      <p class="name-panel__title">Director Craftsman</p>
    </div>
    <div class="contact">
      <p><span class="contact__label">Email : </span>info@marlowecabinets.com.au</p>
      <p><span class="contact__label">Instagram : </span>@marlowe.cabinets</p>
    </div>
    <div class="foot-band"></div>
  </section>
</main>
</body>
</html>
```